Criação de Folder para Alimentos & Bebidas
A empresa queria:
" importamos produtos com nossas marcas e distribuimos para supermercdos e distribuidores "

```html
<!DOCTYPE html>
<html lang="pt-BR">
<head>
<meta charset="utf-8">
<title>Marvale Foods – Folder</title>
<link href="https://fonts.googleapis.com/css2?family=Open+Sans:wght@400;600;700;800&display=swap" rel="stylesheet">
<style>
:root{
  --red:#e0333a;
  --red-dark:#b8242b;
  --yellow:#f2b51c;
  --white:#ffffff;
  --ink:#4a4a4a;
  --bg:#ececec;
  --meat:#a83a3c;
  --meat-dark:#5e2a22;
  --fish:#8a8270;
}
*{box-sizing:border-box;margin:0;padding:0}
html,body{width:1200px;height:1200px;overflow:hidden;background:var(--bg);font-family:"Open Sans",Arial,sans-serif;color:var(--ink)}
.spread{position:absolute;left:195px;width:810px;height:570px;display:flex;box-shadow:0 4px 16px rgba(0,0,0,.15)}
.spread--inside{top:15px}
.spread--outside{top:615px}
.panel{position:relative;width:270px;height:570px;overflow:hidden;background:var(--white)}
.panel+.panel{border-left:1px solid #e4e4e4}
.photo{position:absolute}
.photo--lamb{left:0;right:0;bottom:0;height:170px;background:linear-gradient(135deg,#9a8f80,#d8cfc2 55%,#6d5a48);border-top-right-radius:160px 60px}
.photo--beef{left:0;right:0;top:0;height:290px;background:radial-gradient(circle at 45% 55%,var(--meat) 0,#7e2a2b 45%,var(--meat-dark) 100%)}
.photo--fish{left:0;right:0;bottom:0;height:200px;background:linear-gradient(135deg,#5b5346,var(--fish) 45%,#c9b89a);border-top-left-radius:160px 60px}
.photo--cover{left:0;right:0;top:150px;height:210px;background:radial-gradient(circle at 50% 55%,#b5464a 0,var(--meat) 40%,#3b231c 100%)}
.band{position:absolute;left:0;right:0;height:14px;background:var(--yellow)}
.line-head{position:absolute;left:24px;right:24px}
.line-head .cat{font-size:9px;font-weight:700;letter-spacing:.12em;color:var(--red)}
.line-head .label{font-size:19px;font-weight:700;color:var(--yellow);line-height:1.05}
.line-head .name{font-size:19px;font-weight:700;color:var(--red);line-height:1.1}
.body{position:absolute;font-size:9.5px;line-height:1.55;color:var(--ink)}
.thumbs{position:absolute;display:flex;flex-direction:column;gap:14px}
.thumb{width:54px;height:54px;border-radius:50%;border:3px solid var(--white);box-shadow:0 1px 4px rgba(0,0,0,.25)}
.thumb--lamb1{background:#b8857a}.thumb--lamb2{background:#d9b3ab}.thumb--lamb3{background:#a8574f}
.thumb--fish1{background:#e6d3c4}.thumb--fish2{background:#d7a995}.thumb--fish3{background:#e3b54c}
.photo-title{position:absolute;color:var(--white);font-size:30px;font-weight:700}
.flap-title{position:absolute;left:26px;top:70px;width:220px}
.flap-title .brand{font-size:17px;font-weight:700;color:var(--red)}
.flap-title .tag{font-size:13px;font-weight:700;color:var(--yellow);letter-spacing:.08em}
.back{background:var(--red)}
.back-title{position:absolute;left:26px;top:360px;color:var(--white);font-size:18px;font-weight:700;line-height:1.2}
.contact{position:absolute;left:26px;right:20px;display:flex;gap:10px;align-items:flex-start;color:var(--white);font-size:10px;line-height:1.4}
.contact svg{flex:none}
.contact b{display:block;font-weight:700}
.headline{position:absolute;left:24px;top:28px;font-size:20px;font-weight:700;line-height:1.15}
.headline .y{color:var(--yellow)}
.headline .r{color:var(--red)}
.cover-foot{position:absolute;left:0;right:0;bottom:0;height:220px;background:var(--red)}
.brand-name{position:absolute;left:0;right:0;bottom:80px;text-align:center;color:var(--white);font-size:24px;font-weight:600}
.brand-rule{position:absolute;left:40px;right:40px;bottom:70px;height:1px;background:rgba(255,255,255,.6)}
</style>
</head>
<body>

<section class="spread spread--inside" aria-label="Folder – parte interna">
  <article class="panel">
    <div class="band" style="top:0;height:8px"></div>
    <header class="line-head" style="top:40px">
      <div class="cat">CORDEIROS</div>
      <div class="label">Linha</div>
      <div class="name">Marvale Lamb</div>
    </header>
    <p class="body" style="left:24px;top:130px;width:140px">Cordeiros selecionados de criação natural, com carne macia e sabor suave. Cortes padronizados e embalados a vácuo para supermercados e distribuidores.</p>
    <div class="thumbs" style="right:20px;top:120px">
      <div class="thumb thumb--lamb1" role="img" aria-label="Corte de cordeiro"></div>
      <div class="thumb thumb--lamb2" role="img" aria-label="Carré de cordeiro"></div>
      <div class="thumb thumb--lamb3" role="img" aria-label="Pernil de cordeiro"></div>
    </div>
    <div class="band" style="bottom:170px;height:6px;border-top-right-radius:160px 30px"></div>
    <div class="photo photo--lamb" role="img" aria-label="Foto de cordeiro assado servido"></div>
  </article>

  <article class="panel">
    <div class="photo photo--beef" role="img" aria-label="Foto de cortes bovinos crus"></div>
    <div class="photo-title" style="left:80px;top:215px">Bovinos</div>
    <div class="band" style="top:290px;height:10px"></div>
    <header class="line-head" style="top:325px">
      <div class="cat">BOVINOS</div>
      <div class="label">Linha</div>
      <div class="name">Marvale Beef</div>
    </header>
    <p class="body" style="left:24px;right:24px;top:410px">Cortes bovinos importados com qualidade garantida, maturados e prontos para a sua gôndola.</p>
  </article>

  <article class="panel">
    <div class="band" style="top:0;height:8px"></div>
    <header class="line-head" style="top:40px">
      <div class="cat">PESCADO</div>
      <div class="label">Linha</div>
      <div class="name">Marvale Fish</div>
    </header>
    <p class="body" style="left:24px;top:130px;width:140px">Peixes e frutos do mar congelados logo após a pesca, preservando frescor e textura.</p>
    <div class="thumbs" style="right:20px;top:110px">
      <div class="thumb thumb--fish1" role="img" aria-label="Filé de peixe branco"></div>
      <div class="thumb thumb--fish2" role="img" aria-label="Filé de salmão"></div>
      <div class="thumb thumb--fish3" role="img" aria-label="Camarões"></div>
    </div>
    <div class="photo photo--fish" role="img" aria-label="Foto de peixe inteiro grelhado"></div>
    <div class="photo-title" style="left:110px;bottom:120px">Pescado</div>
  </article>
</section>

<section class="spread spread--outside" aria-label="Folder – parte externa">
  <article class="panel">
    <div class="flap-title">
      <div class="brand">Marvale Foods</div>
      <div class="tag">CARNES NOBRES</div>
    </div>
    <p class="body" style="left:26px;right:26px;top:130px">A Marvale Foods importa produtos com marcas próprias e distribui para supermercados e distribuidores de todo o país.</p>
    <p class="body" style="left:26px;right:26px;top:215px">Trabalhamos com qualidade, logística eficiente e atendimento próximo ao cliente.</p>
    <svg style="position:absolute;left:0;bottom:0" width="270" height="150" viewBox="0 0 270 150" aria-hidden="true">
      <path d="M0 90 Q140 40 270 0 L270 150 L0 150Z" fill="var(--yellow)"/>
      <path d="M0 110 Q140 60 270 25 L270 150 L0 150Z" fill="var(--red)"/>
    </svg>
  </article>

  <article class="panel back">
    <svg style="position:absolute;left:0;top:0" width="270" height="320" viewBox="0 0 270 320" aria-hidden="true">
      <path d="M0 0 H270 V240 Q130 330 0 290Z" fill="var(--white)"/>
      <path d="M0 290 Q130 330 270 240 V252 Q130 342 0 302Z" fill="var(--yellow)"/>
    </svg>
    <div class="back-title">Estamos prontos<br>para lhe atender</div>
    <div class="contact" style="top:440px">
      <svg width="18" height="18" viewBox="0 0 24 24"><circle cx="12" cy="12" r="12" fill="var(--yellow)"/><path d="M8 6l2 0 1 3-1.5 1a7 7 0 0 0 4 4l1-1.5 3 1v2a2 2 0 0 1-2 2A10 10 0 0 1 6 8a2 2 0 0 1 2-2z" fill="var(--white)"/></svg>
      <span><b>Telefone</b>(11) 4000-0000</span>
    </div>
    <div class="contact" style="top:485px">
      <svg width="18" height="18" viewBox="0 0 24 24"><circle cx="12" cy="12" r="12" fill="var(--yellow)"/><path d="M12 5a4 4 0 0 0-4 4c0 3 4 9 4 9s4-6 4-9a4 4 0 0 0-4-4zm0 5.5A1.5 1.5 0 1 1 12 7.5a1.5 1.5 0 0 1 0 3z" fill="var(--white)"/></svg>
      <span><b>Endereço</b>Rua Exemplo, 123 – Cidade, UF</span>
    </div>
  </article>

  <article class="panel">
    <h1 class="headline"><span class="y">Viva a vida<br>de maneira saborosa.</span><br><span class="r">Alimente seu prazer.</span></h1>
    <div class="cover-foot"></div>
    <div class="photo photo--cover" role="img" aria-label="Foto de bife cru com pimentas e ervas"></div>
    <div class="band" style="top:360px;height:8px"></div>
    <div class="brand-name">Marvale Foods</div>
    <div class="brand-rule"></div>
  </article>
</section>

</body>
</html>
```